Advanced Therapeutic Massage Therapist

I need a business card advertising my massage services as an advanced therapeutic massage therapist. I offer advanced therapeutic massage, swedish and deep tissue. I want to create a simple, professional and feminine card. I like bright colours and creativity.

I prefer a bold and experimental approach rather than something status-quo. A card to suggest therapeutic healing through dynamic massage. Motifs, shapes or layout which suggest movement and flow.
Updates

Target Market(s)

Everybody!

Industry/Entity Type

Health And Wellness

Contact Information for Business Card

The card should include:
My name, logo, services offered and my contact details.

Aoibhín Delaney
Massage Therapist

- Swedish - Deep Tissue - Advanced Therapeutic

Phone: (+353) 87 261 9043
Email: regenerate@aoibhindelaney-example.com
Website: www.aoibhindelany-example.com

Font styles to use
Serif
Sans Serif
Decorative
Script

Colors

Designer to choose colors to be used in the design.

Requirements
Must have
• An example may contain something like this, yet concise:
• "Aoibhín Delaney
• Massage Therapist
• - Swedish - Deep Tissue - Advanced Therapeutic"
Nice to have
• This sentence is optional:
• Imagery such as a logo or symbol. I have attached a file containing a logo I had produced however the name is incorrect now as it is "Aoibhín" not "Evie". It could be edited to change it to Aoibhín.
• I have sent the file as .psd .jpg. .pdf and .png
• I like when the card conveys energy, movement, pressure points, flow etc.
• I just like the designer to follow their own style and ideas. I like bright colours but must have a lot of a base colour to offset it. I really prefer them to follow their own inspiration. That is my preference.
Should not have
• Pine trees, non-native trees to Britain and Ireland, exotic flowers or animals that are not native to Britain and Ireland.
• I don't like brown as the background colour of the card.
• The cars shouldn't look like a wedding invitation i.e too many floral type designs.

```html
<!DOCTYPE html>
<html lang="en">
<head>
<meta charset="utf-8">
<title>Aoibhín Delaney – Massage Therapist Business Card</title>
<link rel="stylesheet" href="https://fonts.googleapis.com/css2?family=Work+Sans:wght@300;400;500&display=swap">
<style>
  :root {
    --stage: #2b2b2d;
    --card: #1c1c1d;
    --ink: #f2f2f2;
    --silver: #b9b9bb;
    --gold: #e3a22f;
  }
  html, body {
    margin: 0;
    width: 1200px;
    height: 900px;
    overflow: hidden;
    background: var(--stage);
    font-family: "Work Sans", Arial, sans-serif;
  }
  .canvas {
    width: 1200px;
    height: 900px;
    display: flex;
    flex-direction: column;
    align-items: center;
    justify-content: center;
    gap: 40px;
  }
  .card {
    position: relative;
    width: 680px;
    height: 395px;
    background: var(--card);
    box-shadow: 0 10px 30px rgba(0,0,0,.45);
    color: var(--ink);
    overflow: hidden;
  }

  /* Front */
  .brand {
    position: absolute;
    left: 0; right: 0; top: 70px;
    display: flex;
    flex-direction: column;
    align-items: center;
    gap: 18px;
  }
  .brand-mark {
    width: 150px;
    height: 150px;
    border-radius: 50%;
    border: 2px solid var(--silver);
    box-sizing: border-box;
  }
  .brand-name {
    font-size: 24px;
    font-weight: 400;
    color: var(--silver);
    letter-spacing: .04em;
    white-space: nowrap;
  }
  .tagline {
    position: absolute;
    right: 36px;
    bottom: 26px;
    margin: 0;
    font-size: 14.5px;
    font-weight: 400;
    letter-spacing: .03em;
    color: var(--ink);
    white-space: nowrap;
  }

  /* Back */
  .identity {
    position: absolute;
    left: 40px;
    top: 148px;
    width: 260px;
    text-align: right;
    white-space: nowrap;
  }
  .identity-name {
    margin: 0;
    font-size: 24px;
    line-height: 28px;
    font-weight: 400;
    color: var(--gold);
    letter-spacing: .01em;
  }
  .identity-role {
    margin: 4px 0 0;
    font-size: 15px;
    line-height: 18px;
    font-weight: 400;
    color: var(--ink);
    letter-spacing: .04em;
  }
  .divider {
    position: absolute;
    left: 322px;
    top: 150px;
    width: 2px;
    height: 48px;
    background: var(--ink);
  }
  .contact {
    position: absolute;
    left: 345px;
    top: 152px;
    margin: 0;
    padding: 0;
    list-style: none;
  }
  .contact li {
    display: flex;
    align-items: center;
    gap: 14px;
    font-size: 17px;
    font-weight: 400;
    letter-spacing: .02em;
    line-height: 24px;
    white-space: nowrap;
  }
  .contact svg { width: 13px; height: 13px; flex: none; }
  .services {
    position: absolute;
    left: 95px;
    bottom: 60px;
    margin: 0;
    font-size: 21px;
    font-weight: 400;
    letter-spacing: .03em;
    display: flex;
    align-items: center;
    gap: 10px;
    white-space: nowrap;
  }
  .services .dot {
    width: 8px; height: 8px;
    border-radius: 50%;
    background: var(--gold);
  }
</style>
</head>
<body>
<main class="canvas">

  <section class="card card-front">
    <div class="brand">
      <div class="brand-mark" aria-hidden="true"></div>
      <span class="brand-name">Aoibhín Delaney</span>
    </div>
    <p class="tagline">CTQB qualified specialising in advanced therapeutic and deep tissue massage.</p>
  </section>

  <section class="card card-back">
    <div class="identity">
      <h1 class="identity-name">AOIBHÍN DELANEY</h1>
      <p class="identity-role">MASSAGE THERAPIST</p>
    </div>
    <div class="divider"></div>
    <ul class="contact">
      <li>
        <svg viewBox="0 0 16 16" aria-hidden="true"><path fill="var(--gold)" d="M3.6 1.2l2.3 2.8-1.3 1.8c.9 2 2.4 3.6 4.5 4.6l1.8-1.3 2.9 2.2-1.2 2.7C7.1 14 2 8.9 1 3.2z"/></svg>
        (+353) 87 261 9043
      </li>
      <li>
        <svg viewBox="0 0 16 16" aria-hidden="true"><rect x="1.5" y="3.5" width="13" height="9" fill="none" stroke="var(--gold)" stroke-width="1.5"/><path d="M1.5 3.5l6.5 5 6.5-5" fill="none" stroke="var(--gold)" stroke-width="1.5"/></svg>
        aoibhinmassage@example.com
      </li>
    </ul>
    <p class="services">
      <span>Swedish</span><span class="dot"></span>
      <span>Deep Tissue</span><span class="dot"></span>
      <span>Advanced Therapeutic</span>
    </p>
  </section>

</main>
</body>
</html>
```